Law Firm Business Card

This is a business card for a law firm that serves US military and veterans.

The card must have ONLY the following (we want an uncluttered look):

- Company logo (PNG, GIF, JPEG copies uploaded)
- A tagline reading: "a law firm for service members and veterans"
- My name and title: "Martin Okello" and "Attorney"
- My email: "martin.okello@harborlinecounsel.com"
- My number: "855-FILE-NOW (345-3669)"

We are looking for a clean, simple layout with only the above information, likely printed on a bright white cotton stock. The font of our logo is DIN 1451, and the font used on our website is Helvetica Neue. The color of our logo is #336699, and we probably want the tagline in that color also, and my contact information in a dark grey. Please review our website at www.harborlinecounsel.com to ensure your card design complements our website style.

Thanks and we look forward to seeing your submissions.

A few notes:

- Two-sided submissions are ok
- Please don't add graphics (scales of justice, judges hammer, etc)

```html
<!DOCTYPE html>
<html lang="en">
<head>
<meta charset="utf-8">
<title>Harborline Counsel – Business Card</title>
<link rel="stylesheet" href="https://fonts.googleapis.com/css2?family=Arimo:ital,wght@0,400;0,700;1,400&display=swap">
<style>
  :root {
    --brand-blue: #336699;
    --paper-white: #ffffff;
    --ink-white: #ffffff;
  }
  * { margin: 0; padding: 0; box-sizing: border-box; }
  html, body {
    width: 1200px;
    height: 686px;
    overflow: hidden;
    background: var(--paper-white);
  }
  .card {
    position: relative;
    width: 1200px;
    height: 686px;
    background: var(--paper-white);
    font-family: "Arimo", "Helvetica Neue", Helvetica, Arial, sans-serif;
  }
  .brand-panel {
    position: absolute;
    left: 0;
    top: 0;
    width: 408px;
    height: 686px;
    background: var(--paper-white);
  }
  .brand-name {
    position: absolute;
    left: 168px;
    top: 343px;
    width: 560px;
    transform: translate(-50%, -50%) rotate(-90deg);
    color: var(--brand-blue);
    font-size: 46px;
    font-weight: 700;
    line-height: 1;
    text-align: center;
    white-space: nowrap;
  }
  .tagline {
    position: absolute;
    left: 303px;
    top: 343px;
    width: 640px;
    transform: translate(-50%, -50%) rotate(-90deg);
    color: var(--brand-blue);
    font-size: 30px;
    font-weight: 400;
    line-height: 1;
    white-space: nowrap;
    text-align: center;
  }
  .info-panel {
    position: absolute;
    left: 408px;
    top: 0;
    width: 792px;
    height: 686px;
    background: var(--brand-blue);
    color: var(--ink-white);
  }
  .person-name {
    position: absolute;
    left: 58px;
    top: 160px;
    font-size: 50px;
    font-weight: 400;
    line-height: 1.1;
    white-space: nowrap;
  }
  .person-title {
    position: absolute;
    left: 60px;
    top: 226px;
    font-size: 32px;
    font-style: italic;
    font-weight: 400;
    white-space: nowrap;
  }
  .contact {
    position: absolute;
    left: 186px;
    top: 422px;
    font-size: 33px;
    font-weight: 400;
    line-height: 1.3;
    font-style: normal;
    white-space: nowrap;
  }
  .contact span { display: block; }
</style>
</head>
<body>
  <main class="card">
    <section class="brand-panel">
      <p class="brand-name">Harborline Counsel</p>
      <p class="tagline">A law firm for service members and veterans</p>
    </section>
    <section class="info-panel">
      <h1 class="person-name">Martin Okello</h1>
      <p class="person-title">Attorney</p>
      <address class="contact">
        <span class="contact-phone">855-FILE-NOW (345-3669)</span>
        <span class="contact-email">martin.okello@harborlinecounsel.com</span>
      </address>
    </section>
  </main>
</body>
</html>
```